Anzeigengestaltung für Gebäudedienstleistungsunternehmen
Zielgruppe
Wir sind ein lokales Gebäudedienstleistungsunternehmen und bieten Gebäudereinigung und Haushaltsreinigung, Grünanlagenpflege und Gartenpflege, Winterdienst und Hausmeisterservice für Privat- und Gewerbekunden an.
Aufgabenstellung
Zur Info: Wir benötigen auch ein Flyerdesign. Dieses möchten wir in Anschluss an diesen Auftrag als 1-zu-1 Projekt an den Designer unserer Anzeige vergeben.
Diese Anzeige soll in dem lokalen Mitteilungsblatt (https://www.ortsbote-velun.com/index.php) erscheinen.
Es ist eine farbige zweispaltige (92mm) Anzeige mit der Höhe von 50mm.
Unser Logo und die Firmenfarben sollen verwendet werden. Gerne darf auch ein Foto benutzt werden (z.B. im Hintergrund), welches nach den Jahreszeiten gewechselt werden kann. Zum Beispiel: Frühjahr -> Gartenpflege, Sommer -> Gebäudereinigung, Herbst -> Winterdienst und im Winter -> Hausmeisterservice.
Der Text sollte unsere Dienstleistungen enthalten. Diese sind: Gebäude- und Haushaltsreinigung, Grünanlagen- und Gartenpflege, Winterdienst und Hausmeisterservice. Zusätzlich der Hinweis, dass wir sowohl Privat als auch Gewerbekunden ansprechen möchten.
Unsere Kontaktdaten sollen auch enthalten sein:
Internet: www.brimato.de, Telefon: 09471/3582140, E-Mail: kontakt@brimato.de
Falls es noch Platz gibt, dann wäre es schön noch den lokalen Bezug herzustellen, indem man die Postleitzahl und den Ort unserer Firma nennt. Eine Nennung der Straße ist nicht vorgesehen.
PLZ: 91207 Ort: Lauf an der Pegnitz od. Lauf a.d. Pegnitz

```html
<!DOCTYPE html>
<html lang="de">
<head>
<meta charset="utf-8">
<title>Brimato Gebäudedienste – Anzeige</title>
<link rel="stylesheet" href="https://fonts.googleapis.com/css2?family=Montserrat:wght@800;900&family=Heebo:wght@300&family=Roboto+Condensed:wght@400;700&family=Open+Sans:wght@400&display=swap">
<style>
  :root {
    --brand-blue: #0270ab;
    --panel-blue: rgba(8, 96, 150, 0.9);
    --page-bg: #f1f1f1;
    --white: #ffffff;
  }
  * { margin: 0; padding: 0; box-sizing: border-box; }
  html, body { width: 1166px; height: 1200px; overflow: hidden; background: var(--page-bg); }
  .ad {
    position: absolute; left: 33px; top: 301px;
    width: 1100px; height: 598px;
    background: var(--brand-blue);
    overflow: hidden;
  }
  .ad__photo {
    position: absolute; left: 0; top: 0; width: 1100px; height: 517px;
    background:
      linear-gradient(90deg, rgba(20,40,30,0) 55%, rgba(210,215,220,0.55) 80%, rgba(235,238,240,0.7) 100%),
      linear-gradient(180deg, #3d5a36 0%, #4d6e3c 35%, #2f3d2c 65%, #8a8378 100%);
  }
  .ad__panel { position: absolute; left: 0; top: 0; }
  .ad__content { position: absolute; left: 22px; top: 0; color: var(--white); }
  .ad__headline {
    position: absolute; left: 0; top: 20px;
    font: 900 63px/1 "Montserrat", sans-serif; letter-spacing: -0.8px;
    text-shadow: 0 3px 10px rgba(0,0,0,0.35); white-space: nowrap;
  }
  .ad__services {
    position: absolute; left: 0; top: 118px; width: 560px;
    font: 300 29px/35px "Heebo", sans-serif;
  }
  .ad__audience {
    position: absolute; left: 0; top: 272px;
    font: 700 29px/1 "Roboto Condensed", sans-serif; white-space: nowrap;
  }
  .ad__call {
    position: absolute; left: 0; top: 343px;
    font: 400 28px/1 "Roboto Condensed", sans-serif; white-space: nowrap;
  }
  .ad__phone {
    position: absolute; left: 0; top: 381px;
    font: 700 51px/1 "Roboto Condensed", sans-serif; white-space: nowrap;
  }
  .ad__email {
    position: absolute; left: 2px; top: 444px;
    font: 700 33px/1 "Roboto Condensed", sans-serif; white-space: nowrap;
  }
  .ad__footer {
    position: absolute; left: 0; top: 517px; width: 1100px; height: 81px;
    background: var(--brand-blue); color: var(--white);
  }
  .ad__website {
    position: absolute; left: 31px; top: 18px;
    font: 400 37px/1 "Open Sans", sans-serif;
  }
  .brand { position: absolute; right: 19px; top: 16px; display: flex; align-items: center; gap: 12px; }
  .brand__mark { width: 44px; height: 44px; background: var(--white); }
  .brand__name {
    font: 900 23px/25px "Montserrat", sans-serif; text-transform: uppercase; letter-spacing: 0.5px;
  }
</style>
</head>
<body>
  <section class="ad">
    <div class="ad__photo" role="img" aria-label="Foto: Gärtner mit Motorsense mäht Rasen vor einem hellen Haus mit Palme und Hecke"></div>
    <svg class="ad__panel" width="1100" height="517" viewBox="0 0 1100 517">
      <polygon points="0,0 596,0 435,489 0,489" fill="var(--panel-blue)"/>
    </svg>
    <div class="ad__content">
      <h1 class="ad__headline">Alles rund um Ihre Immobilie</h1>
      <p class="ad__services">Nutzen Sie unseren full-service rund um Gebäude- und Haushaltsreinigung, Grünanlagen- und Gartenpflege, Winterdienst und Hausmeisterservice.</p>
      <p class="ad__audience">Für Privat- und Gewerbekunden!</p>
      <p class="ad__call">RUFEN SIE UNS GERNE AN!</p>
      <p class="ad__phone">09471 358 2140</p>
      <p class="ad__email">kontakt@brimato.de</p>
    </div>
    <footer class="ad__footer">
      <p class="ad__website">www.brimato.de</p>
      <div class="brand">
        <span class="brand__mark"></span>
        <span class="brand__name">Brimato<br>Gebäudedienste</span>
      </div>
    </footer>
  </section>
</body>
</html>
```